Company or website name
- The Quillstone Movers and Storage
- Links to the website
- Quillstonehauling.com
- Describe your company and organization and target audience
- Residential and commercial moving and relocation service that needs a website redesign.
- The design should have the following
- I NEED THE WEBSITE TO BE SIMPLE AND STRAIGHT TO THE POINT...MAIN CONCERN IS THAT THEY FILL OUT INFORMATION TO GET QUOTE. SITE EXAMPLE THAT I LIKE IS ( WWW.MYPELDRAN.COM) https://www.orvikhaulage.com/

```html
<!DOCTYPE html>
<html lang="en">
<head>
<meta charset="utf-8">
<title>Quillstone Movers and Storage</title>
<link href="https://fonts.googleapis.com/css2?family=Oswald:wght@500;700&family=Roboto:wght@400;700;900&family=Open+Sans:ital,wght@0,400;0,600;0,700;1,400&display=swap" rel="stylesheet">
<style>
:root{
  --navy:#1d2b4f;
  --blue:#2b4a8f;
  --red:#e8243f;
  --coral:#f0606a;
  --text:#5a5a5a;
  --light:#f8f8f8;
  --line:#d9d9d9;
  --dark:#262b3a;
}
*{box-sizing:border-box;margin:0;padding:0}
html,body{width:1200px;height:4933px;overflow:hidden}
body{position:relative;font-family:"Open Sans",sans-serif;color:var(--text);background:#fff}
.abs{position:absolute}
.h2{font-family:"Roboto",sans-serif;font-weight:900;color:var(--navy);font-size:31px;letter-spacing:-0.5px}
.h2 span{color:var(--red)}
.p{font-size:11.5px;line-height:21px}
.btn{position:absolute;display:flex;align-items:center;justify-content:center;color:#fff;font-family:"Open Sans",sans-serif;font-weight:700;font-size:10px;letter-spacing:1px;text-transform:uppercase}

/* top bar */
.topbar{left:0;top:0;width:1200px;height:20px;background:var(--blue);color:#fff;font-size:9px;font-weight:600}
.topbar .contact{left:210px;top:4px;display:flex;gap:10px}
.social{right:207px;top:5px;display:flex;gap:9px}
.social i{width:10px;height:10px;border-radius:50%;background:#fff;display:block}

/* hero */
.hero{left:0;top:20px;width:1200px;height:537px;background:linear-gradient(180deg,#d6dbd2 0%,#c8cfc3 55%,#a9b79a 100%)}
.logo{left:212px;top:35px;display:flex;align-items:center;gap:8px;font-family:"Roboto",sans-serif;font-weight:900;font-size:24px;letter-spacing:3px;color:var(--blue)}
.logo i{width:16px;height:16px;border-radius:50%;background:var(--navy);display:block}
.nav{left:514px;top:44px;display:flex;gap:26px;font-size:10.5px;color:var(--navy);font-weight:600}
.hero-title{left:0;top:188px;width:1200px;text-align:center;font-family:"Oswald",sans-serif;font-weight:700;font-size:58px;color:var(--red);letter-spacing:1px}
.hero-sub{left:0;top:262px;width:1200px;text-align:center;font-family:"Roboto",sans-serif;font-size:20px;color:var(--navy)}
.hero-btn{left:533px;top:319px;width:124px;height:34px;background:var(--coral);border-radius:2px;text-transform:none;letter-spacing:.3px;font-size:11px}

/* quote form */
.quote{left:203px;top:496px;width:264px;height:333px;background:var(--blue);border-radius:5px}
.quote h3{position:absolute;left:0;top:20px;width:264px;text-align:center;font-family:"Roboto",sans-serif;font-weight:700;color:#fff;font-size:17px}
.field{position:absolute;background:#fff;border-radius:2px;font-size:8.5px;color:#9a9a9a;padding:6px 10px}
.send{left:20px;top:288px;width:64px;height:22px;background:var(--red)}

/* about */
.about-title{left:547px;top:620px}
.about-text{left:547px;top:664px;width:450px}
.about-btn{left:547px;top:800px;width:132px;height:31px;background:var(--coral)}

/* families */
.band-gray{left:0;top:928px;width:1200px;height:463px;background:var(--light)}
.fam-kicker{left:210px;top:1020px;font-size:9px}
.fam-title{left:210px;top:1034px;width:380px;font-family:"Roboto",sans-serif;font-weight:700;font-size:17px;line-height:25px;color:var(--red)}
.fam-title b{color:var(--navy)}
.fam-h{font-weight:700;font-size:10.5px;color:#444;text-transform:uppercase}
.fam-img{left:617px;top:1038px;width:371px;height:227px;background:linear-gradient(180deg,#c9dbe9 0%,#e8ecef 50%,#7ea36a 100%)}

/* resources */
.res-title{left:0;top:1467px;width:1200px;text-align:center}

/* secure */
.band-secure{left:0;top:1795px;width:1200px;height:439px;background:#fbfbfb}
.secure-img{left:210px;top:1889px;width:370px;height:246px;background:linear-gradient(135deg,#dfe3e6,#8b96a3 55%,#2a3344)}
.secure-title{left:610px;top:1887px}
.secure-text{left:610px;top:1932px;width:380px}
.secure-btn{left:610px;top:2108px;width:111px;height:33px;background:linear-gradient(90deg,#e0577d,#f07a5f)}

/* reviews */
.reviews{left:0;top:2234px;width:1200px;height:560px;background:linear-gradient(90deg,#3b4153 0%,#4a4e5c 50%,#6a6470 100%)}
.reviews-title{left:0;top:2322px;width:1200px;text-align:center;color:#fff}
.quote-mark{left:585px;top:2450px}
.review-text{left:340px;top:2500px;width:520px;text-align:center;font-style:italic;color:#e9e9ee;font-size:13.5px;line-height:23px}
.avatar{left:565px;top:2558px;width:70px;height:70px;background:linear-gradient(180deg,#c8b8ad,#6e5a52);border:2px solid #fff}
.reviewer{left:0;top:2645px;width:1200px;text-align:center;color:var(--red);font-size:8px;font-weight:600}
.stars{left:0;top:2667px;width:1200px;text-align:center;color:#f3b618;font-size:12px;letter-spacing:2px}

/* track */
.track-title{left:210px;top:2998px}
.track-text{left:210px;top:3042px;width:380px}
.track-btn{left:210px;top:3186px;width:106px;height:33px;background:linear-gradient(90deg,#e0577d,#f07a5f)}
.track-img{left:632px;top:2871px;width:335px;height:473px;background:linear-gradient(160deg,#a45a3a,#c98660 50%,#6b3d2a);box-shadow:0 4px 14px rgba(0,0,0,.2)}

/* rates */
.rates{left:0;top:3420px;width:1200px;height:747px;background:linear-gradient(90deg,#252a3c 0%,#3b3f50 50%,#4c4a55 100%)}
.rates-title{left:0;top:3500px;width:1200px;text-align:center;color:#fff}
.rates-sub{left:0;top:3545px;width:1200px;text-align:center;color:#fff;font-size:11px}
.card{position:absolute;top:3732px;width:247px;height:351px;background:#fff}
.card .name{position:absolute;top:16px;width:100%;text-align:center;font-family:"Oswald",sans-serif;font-weight:700;font-size:20px;color:var(--navy)}
.card .crew{position:absolute;top:50px;width:100%;text-align:center;font-size:10.5px;color:var(--blue)}
.card .price{position:absolute;top:78px;width:100%;height:84px;background:#f4f4f4}
.card .amt{position:absolute;top:17px;width:100%;text-align:center;font-family:"Oswald",sans-serif;font-weight:500;font-size:28px;color:var(--navy)}
.card .per{position:absolute;top:57px;width:100%;text-align:center;font-size:9px}
.card ul{position:absolute;top:182px;width:100%;list-style:none;text-align:center;font-size:9.5px;line-height:25px}
.card .book{left:80px;top:297px;width:86px;height:26px;background:var(--navy);font-size:9.5px}

/* contact */
.touch-title{left:0;top:4245px;width:1200px;text-align:center}
.touch-sub{left:390px;top:4292px;width:420px;text-align:center;font-size:11px;line-height:20px}
.lbl{position:absolute;left:363px;font-size:10px;color:#555}
.inp{position:absolute;left:363px;width:222px;height:30px;border:1px solid var(--line)}
.submit{left:363px;top:4756px;width:70px;height:26px;background:var(--navy);text-transform:none;letter-spacing:0;font-size:11px}

/* footer */
.footer{left:0;top:4823px;width:1200px;height:110px;background:var(--navy)}
.copy{left:212px;top:4880px;font-size:9px;color:#8a92a8}
.flinks{left:845px;top:4880px;display:flex;gap:14px;font-size:9px;color:#fff}
.totop{left:1152px;top:4810px;width:24px;height:24px;border-radius:50%;background:#fff;border:2px solid var(--navy)}
</style>
</head>
<body>

<div class="abs topbar">
  <div class="abs contact">
    <span>&#9742; (555) 014-2290</span>
    <span>&#9993; info@quillstonehauling.com</span>
  </div>
  <div class="abs social"><i></i><i></i><i></i><i></i></div>
</div>

<div class="abs hero" role="img" aria-label="Photo of a moving truck parked in front of a house"></div>
<div class="abs logo"><i></i>QUILLSTONE</div>
<nav class="abs nav"><span>HOME</span><span>ABOUT</span><span>HOW IT WORKS</span><span>REVIEWS</span><span>TRACKING</span><span>PRICING</span><span>CONTACTS</span></nav>
<h1 class="abs hero-title">WE HELP MOVE LIVES FORWARD</h1>
<p class="abs hero-sub">Providing Local, Long Distance Residential and Commercial Moving Services Since 2006</p>
<div class="btn hero-btn">Free Quote Now</div>

<form class="abs quote">
  <h3>GET INSTANT QUOTE</h3>
  <div class="field" style="left:20px;top:65px;width:224px;height:26px">Full Name</div>
  <div class="field" style="left:20px;top:100px;width:109px;height:26px">E-mail</div>
  <div class="field" style="left:135px;top:100px;width:109px;height:26px">Phone</div>
  <div class="field" style="left:20px;top:135px;width:109px;height:26px">Select Type</div>
  <div class="field" style="left:135px;top:135px;width:109px;height:26px">dd/mm/yyyy</div>
  <div class="field" style="left:20px;top:170px;width:109px;height:26px">From</div>
  <div class="field" style="left:135px;top:170px;width:109px;height:26px">To</div>
  <div class="field" style="left:20px;top:205px;width:224px;height:70px">Additional Info</div>
  <div class="btn send">SEND</div>
</form>

<h2 class="abs h2 about-title">ABOUT <span>QUILLSTONE</span></h2>
<p class="abs p about-text">At Quillstone Inc we coordinate local, long distance moves that incorporate all the necessary moving services to est serve your individual move. In addition, we offer our commercial clients a wide array of specialized transportation services for high-value products. We are committed to safe, simple moving experiences for family, businesses and employees.</p>
<div class="btn about-btn">LEARN MORE</div>

<div class="abs band-gray"></div>
<div class="abs fam-kicker">WE</div>
<h3 class="abs fam-title"><b>MOVING FAMILIES &amp;</b> BUSINESSES FOR OVER A DECADE</h3>
<div class="abs" style="left:210px;top:1090px;width:380px">
  <p class="p">As movers since 2007, Quillstone Inc has an expertise in transportation and storage services that is unequaled by other moving companies.</p>
  <p class="fam-h" style="margin-top:10px">Moving Services</p>
  <p class="p">From transporting a single household to corporate and government transfers. Quillstone Inc is equipped to handle your needs.</p>
  <p class="fam-h" style="margin-top:10px">Areas Served</p>
  <p class="p">Our expansive network of offices provides us with a broad scope of capabilities to best serve our customers' unique moving and storage needs.</p>
</div>
<div class="abs fam-img" role="img" aria-label="Photo of a semi truck with moving trailer outside a home"></div>

<h2 class="abs h2 res-title">MOVING <span>RESOURCES</span></h2>

<div class="abs band-secure"></div>
<div class="abs secure-img" role="img" aria-label="Photo of a mover in a branded shirt walking through an office"></div>
<h2 class="abs h2 secure-title">SECURE AND <span>INSURED</span></h2>
<div class="abs secure-text">
  <p class="p">Turpis tincidunt id aliquet risus feugiat in. Ut sem viverra aliquet eget sited adipiscing diam donec adipiscing tristique risus nec. In aliquam sem fringilla ut morbi.</p>
  <p class="p" style="margin-top:12px">Egestas fringilla phasellus faucibus scelerisque eleifend donec pretium pellentesque dignissim enim sit amet venenatis urna cursus eget. At augue eget arcu dictum varius duis maecenas sed enim ut sem viverra aliquet eget sit.</p>
</div>
<div class="btn secure-btn">GET STARTED</div>

<div class="abs reviews" role="img" aria-label="Photo of a happy couple unpacking moving boxes"></div>
<h2 class="abs h2 reviews-title" style="color:#fff">CLIENTS <span>REVIEWS</span></h2>
<svg class="abs quote-mark" width="30" height="24" viewBox="0 0 30 24"><path fill="#d8d8de" d="M0 24V13C0 5 4 1 12 0v5c-4 1-6 3-6 7h6v12zM17 24V13c0-8 4-12 12-13v5c-4 1-6 3-6 7h6v12z"/></svg>
<p class="abs review-text">Duis aute irure dolor in reprehenderit in voluptate velit esse cillum dolore eu fugiat nulla pariatur.</p>
<div class="abs avatar" role="img" aria-label="Portrait of the reviewer"></div>
<div class="abs reviewer">Mara Ellis</div>
<div class="abs stars">&#9733;&#9733;&#9733;&#9733;&#9733;</div>

<h2 class="abs h2 track-title">TRACK IT <span>ANYWHERE</span></h2>
<p class="abs p track-text">Zullam nulla eros ultricies sit amet nonummy id imperdiet feugiat peded lectus mollis hendrerit risus nec sem in justo pellentesque facilisis. Etiam imperdiet imperdiet orciunc nec neque leo dolor tempus non auctor hendrerit quis nisi. Curabitur ligula sapien tincidunt non euismod vitae posuere imperdiet leoae cenas malesuada. Praesent congue erat at massa cursus turpis vitae tortor.</p>
<div class="btn track-btn">CONTACT US</div>
<div class="abs track-img" role="img" aria-label="Photo of a hand holding a phone showing a tracking map"></div>

<div class="abs rates" role="img" aria-label="Photo of a family packing boxes at home"></div>
<h2 class="abs h2 rates-title" style="color:#fff">OUR BEST <span>RATES</span></h2>
<p class="abs rates-sub">Nulla tristique urna id lacinia egestas sapien arcu convallis velit id porta turpis velit molestie enim sagittis.</p>

<div class="card" style="left:216px">
  <div class="name">SMALLER MOVES</div><div class="crew">2 Movers 1 Small Truck</div>
  <div class="price"><div class="amt">$300</div><div class="per">Per Hour</div></div>
  <ul><li>Fully Uniformed Movers</li><li>Fully Licensed &amp; Insured</li><li>Tracked Inventory</li><li>Any Location (US)</li></ul>
  <div class="btn book">BOOK NOW</div>
</div>
<div class="card" style="left:477px">
  <div class="name">REGULAR MOVES</div><div class="crew">4 Movers 1 Medium Truck</div>
  <div class="price"><div class="amt">$400</div><div class="per">Per Hour</div></div>
  <ul><li>Fully Uniformed Movers</li><li>Fully Licensed &amp; Insured</li><li>Tracked Inventory</li><li>Any Location (US)</li></ul>
  <div class="btn book">BOOK NOW</div>
</div>
<div class="card" style="left:737px">
  <div class="name">BIG MOVES</div><div class="crew">6 Movers 1 Big Truck</div>
  <div class="price"><div class="amt">$500</div><div class="per">Per Hour</div></div>
  <ul><li>Fully Uniformed Movers</li><li>Fully Licensed &amp; Insured</li><li>Tracked Inventory</li><li>Any Location (US)</li></ul>
  <div class="btn book">BOOK NOW</div>
</div>

<h2 class="abs h2 touch-title">GET IN <span>TOUCH</span></h2>
<p class="abs touch-sub">Nulla tristique urna id lacinia egestas sapien arcu convallis velit id porta turpis velit molestie enim sagittis.</p>
<span class="lbl" style="top:4390px">Your name</span><div class="inp" style="top:4406px"></div>
<span class="lbl" style="top:4455px">Your email</span><div class="inp" style="top:4471px"></div>
<span class="lbl" style="top:4519px">Subject</span><div class="inp" style="top:4535px"></div>
<span class="lbl" style="top:4584px">Your message (optional)</span><div class="inp" style="top:4600px;width:230px;height:140px"></div>
<div class="btn submit">Submit</div>

<footer class="abs footer"></footer>
<div class="abs copy">Copyright © QUILLSTONE | All rights reserved.</div>
<div class="abs flinks"><span>Privacy</span><span>/</span><span>Terms</span><span>/</span><span>Cookies</span></div>
<svg class="abs totop" viewBox="0 0 24 24"><path d="M12 7v10M8 11l4-4 4 4" stroke="#1d2b4f" stroke-width="1.6" fill="none"/></svg>

</body>
</html>
```